Email Signature - GILDED HARBOUR STAYS

Hi there,

I'm after an email signature for my email. I have attached a sample of what I like to this brief (File name: "Email Signature Sample").

I would like my email signature to have the following information:

Rosalind Vetterby
GILDED HARBOUR STAYS
Mobile: 0437 291 604 ( Australia )
Tel: +61 437 291 604 ( International )
Email: rosalind@gildedharbourstays.com
Website: www.gildedharbourstayscom

Industry/Entity Type

Online

Requirements
Must have
• I would like the signature to have a professional look

```html
<!DOCTYPE html>
<html lang="en">
<head>
<meta charset="utf-8">
<title>Email Signature – Gilded Harbour Stays</title>
<link href="https://fonts.googleapis.com/css2?family=Arimo:wght@400;700&display=swap" rel="stylesheet">
<style>
  :root {
    --page-bg: #ffffff;
    --ink: #1f1f1f;
    --brand-blue: #1778c2;
    --sun-orange: #f7a12b;
  }
  html, body {
    margin: 0;
    padding: 0;
    width: 1200px;
    height: 1000px;
    overflow: hidden;
    background: var(--page-bg);
    font-family: "Arimo", Arial, sans-serif;
    color: var(--ink);
  }
  .signature {
    position: absolute;
    left: 177px;
    top: 263px;
    width: 845px;
    height: 474px;
  }
  .brand-dot {
    position: absolute;
    left: 470px;
    top: 26px;
    width: 140px;
    height: 140px;
  }
  .sig-name {
    position: absolute;
    left: 38px;
    top: 126px;
    margin: 0;
    font-size: 32px;
    font-weight: 700;
    letter-spacing: 0.5px;
  }
  .sig-rule {
    position: absolute;
    left: 38px;
    top: 167px;
    width: 582px;
    height: 3px;
    background: var(--ink);
  }
  .brand-name {
    position: absolute;
    left: 38px;
    top: 172px;
    margin: 0;
    font-size: 42px;
    font-weight: 700;
    color: var(--brand-blue);
    letter-spacing: 0.5px;
    white-space: nowrap;
  }
  .contact-list {
    position: absolute;
    left: 38px;
    top: 258px;
    margin: 0;
    padding: 0;
    list-style: none;
    font-size: 29px;
    line-height: 35px;
  }
  .contact-list .label { font-weight: 700; }
  .website {
    position: absolute;
    left: 38px;
    top: 406px;
    margin: 0;
    font-size: 29px;
    font-weight: 700;
  }
</style>
</head>
<body>
  <section class="signature" aria-label="Email signature">
    <svg class="brand-dot" viewBox="0 0 140 140" aria-hidden="true">
      <circle cx="70" cy="70" r="68" fill="var(--sun-orange)"/>
    </svg>
    <p class="sig-name">Rosalind Vetterby</p>
    <div class="sig-rule"></div>
    <p class="brand-name">GILDED HARBOUR STAYS</p>
    <ul class="contact-list">
      <li><span class="label">M:</span> 0437 291 604 ( Australia )</li>
      <li><span class="label">T:</span> +61 437 291 604 ( International )</li>
      <li><span class="label">E:</span> rosalind@gildedharbourstays.com</li>
    </ul>
    <p class="website">www.gildedharbourstayscom</p>
  </section>
</body>
</html>
```